Marine Business Card

We install Lighting, Sound, Video, PA Systems to hotels, nightclubs, Restaurants, Cruise Ships.

Target Market(s)

We want to focus on the Marine or Maritime/Cruise industry. Passenger ships and cruise liners are the companies we want to appeal to

Industry/Entity Type

Business

Contact Information for Business Card

Mark Dellow
Managing Director
Harbourne Beam and Audio Marine Ltd

Requirements
Must have
• Office: 01632 960418
Mobile: 07700 900371
mark@harbournebeamandaudio.co.uk
www.harbournebeamandaudio.co.uk

```html
<!DOCTYPE html>
<html lang="en">
<head>
<meta charset="utf-8">
<title>Harbourne Beam &amp; Audio Marine Ltd – Business Card</title>
<link rel="stylesheet" href="https://fonts.googleapis.com/css2?family=Della+Respira&family=Marcellus&display=swap">
<style>
  :root {
    --page: #ffffff;
    --card: #231f20;
    --band: #363334;
    --band-edge: #4a4748;
    --gold: #f7d77a;
    --gold-dark: #9b6f2a;
    --gold-light: #f3d08a;
    --white: #ffffff;
    --silver-light: #f2f2f2;
    --silver-dark: #7d7d7d;
    --accent-strip: #3a2a2e;
  }
  html, body {
    margin: 0;
    padding: 0;
    width: 1200px;
    height: 1000px;
    overflow: hidden;
    background: var(--page);
  }
  .canvas {
    position: relative;
    width: 1200px;
    height: 1000px;
  }
  .card {
    position: absolute;
    left: 73px;
    top: 157px;
    width: 1035px;
    height: 680px;
    background: var(--card);
  }
  .side-pattern {
    position: absolute;
    left: 955px;
    width: 80px;
    background: linear-gradient(180deg, #4a3a3a 0%, var(--accent-strip) 50%, #33313a 100%);
  }
  .side-pattern--top { top: 0; height: 225px; }
  .side-pattern--bottom { top: 393px; height: 287px; }
  .feature-band {
    position: absolute;
    left: -4px;
    top: 225px;
    width: 961px;
    height: 168px;
    background: radial-gradient(ellipse at 50% 50%, #3e3b3c 0%, var(--band) 70%);
    border-left: 4px solid var(--band-edge);
  }
  .contact-details {
    position: absolute;
    left: 0;
    top: 225px;
    width: 957px;
    height: 168px;
    margin: 0;
    display: flex;
    flex-direction: column;
    justify-content: center;
    align-items: center;
    gap: 8px;
    font-family: "Della Respira", serif;
    font-size: 27px;
    line-height: 1.2;
    color: var(--white);
    font-style: normal;
  }
  .contact-details .label { color: var(--gold); }
  .contact-details .sep { color: var(--gold); padding: 0 14px; }
  .ornament {
    position: absolute;
    top: 50px;
    width: 80px;
    height: 30px;
    border-radius: 15px;
    background: linear-gradient(90deg, rgba(220,220,220,0.15), rgba(220,220,220,0.45), rgba(220,220,220,0.15));
  }
  .ornament--left { left: 42px; }
  .ornament--right { left: 913px; }
  .company-name {
    position: absolute;
    left: 0;
    top: 58px;
    width: 1000px;
    margin: 0;
    text-align: center;
    font-family: "Marcellus", serif;
    font-weight: 400;
    font-size: 44px;
    letter-spacing: 0.5px;
    line-height: 1;
    background: linear-gradient(180deg, var(--silver-light) 0%, #cfcfcf 45%, var(--silver-dark) 100%);
    -webkit-background-clip: text;
    background-clip: text;
    color: transparent;
  }
  .divider {
    position: absolute;
    display: block;
  }
  .divider--title { left: 134px; top: 110px; }
  .divider--services { left: 258px; top: 434px; }
  .contact-name {
    position: absolute;
    left: 145px;
    top: 176px;
    margin: 0;
    font-family: "Della Respira", serif;
    font-weight: 400;
    font-size: 44px;
    letter-spacing: 1px;
    line-height: 1;
    color: var(--gold);
    white-space: nowrap;
  }
  .services-intro {
    position: absolute;
    left: 0;
    top: 400px;
    width: 1000px;
    margin: 0;
    text-align: center;
    font-family: "Della Respira", serif;
    font-size: 34px;
    line-height: 1;
    color: var(--white);
  }
  .services {
    position: absolute;
    left: 0;
    top: 470px;
    width: 1035px;
    margin: 0;
    font-family: "Della Respira", serif;
    font-size: 44px;
    letter-spacing: 2px;
    color: var(--gold);
    line-height: 1;
    white-space: nowrap;
  }
  .services span { position: absolute; }
  .services .line-1 { left: 92px; top: 0; }
  .services .line-2 { left: 118px; top: 65px; }
  .services .line-3 { left: 347px; top: 121px; }
</style>
</head>
<body>
<div class="canvas">
  <section class="card">
    <div class="side-pattern side-pattern--top" role="img" aria-label="Decorative multicoloured circle pattern strip"></div>
    <div class="side-pattern side-pattern--bottom" role="img" aria-label="Decorative multicoloured circle pattern strip"></div>
    <div class="feature-band" role="img" aria-label="Decorative band of grey overlapping circles and ship wheels"></div>

    <address class="contact-details">
      <span><span class="label">Office:</span> 01632 960418<span class="sep">|</span><span class="label">Mobile:</span> 07700 900371</span>
      <span>mark@harbournebeamandaudio.co.uk</span>
      <span>www.harbournebeamandaudio.co.uk</span>
    </address>

    <div class="ornament ornament--left" role="img" aria-label="Silver flourish ornament"></div>
    <div class="ornament ornament--right" role="img" aria-label="Silver flourish ornament"></div>

    <h1 class="company-name">Harbourne Beam &amp; Audio Marine Ltd</h1>

    <svg class="divider divider--title" width="735" height="30" viewBox="0 0 735 30" aria-hidden="true">
      <defs>
        <linearGradient id="goldRule" x1="0" x2="1" y1="0" y2="0">
          <stop offset="0" stop-color="#231f20"/>
          <stop offset="0.5" stop-color="#f3d08a"/>
          <stop offset="1" stop-color="#9b6f2a"/>
        </linearGradient>
        <linearGradient id="goldRuleR" x1="0" x2="1" y1="0" y2="0">
          <stop offset="0" stop-color="#9b6f2a"/>
          <stop offset="0.5" stop-color="#f3d08a"/>
          <stop offset="1" stop-color="#231f20"/>
        </linearGradient>
        <linearGradient id="goldGem" x1="0" x2="1" y1="0" y2="1">
          <stop offset="0" stop-color="#f6dc9a"/>
          <stop offset="0.5" stop-color="#c08a3a"/>
          <stop offset="1" stop-color="#7a5220"/>
        </linearGradient>
      </defs>
      <rect x="0" y="14" width="332" height="3" fill="url(#goldRule)"/>
      <polygon points="324,15.5 332,9.5 340,15.5 332,21.5" fill="#b5822f"/>
      <polygon points="367,0 387,15.5 367,31 347,15.5" fill="url(#goldGem)"/>
      <polygon points="395,15.5 403,9.5 411,15.5 403,21.5" fill="#b5822f"/>
      <rect x="403" y="14" width="332" height="3" fill="url(#goldRuleR)"/>
    </svg>

    <p class="contact-name">Mark Dellow-Managing Director</p>

    <p class="services-intro">We install</p>

    <svg class="divider divider--services" width="484" height="26" viewBox="0 0 484 26" aria-hidden="true">
      <rect x="0" y="12" width="218" height="2" fill="url(#goldRule)"/>
      <polygon points="212,13 219,8 226,13 219,18" fill="#b5822f"/>
      <polygon points="242,0 255,13 242,26 229,13" fill="url(#goldGem)"/>
      <polygon points="258,13 265,8 272,13 265,18" fill="#b5822f"/>
      <rect x="266" y="12" width="218" height="2" fill="url(#goldRuleR)"/>
    </svg>

    <p class="services">
      <span class="line-1">* Lighting, Sound, Video, PA Systems for *</span>
      <span class="line-2">Hotels, Nightclubs, Restaurants &amp;</span>
      <span class="line-3">Cruise Ships</span>
    </p>
  </section>
</div>
</body>
</html>
```